Redesign of corporate card

We need a double sided card designed to use for all our REALTORS. We are a real estate Brokerage firm in Ottawa, Ontario Canada. Our cards will have our logo on them. The information on the card for is one is as follows: Norma Castell, Broker. Fernhollow Realty, Brokerage. (613) 555-0192 Ext 3. ncastell@fernhollow.ca. www.normacastell.ca. Attached is our logo, agent picture.

Most of the back should be used for a note.

We have included a proof of our sign. Should have some of the characteristics of the sign.

Reason: I have asked for changes several times but as of now the changes have not been made, nor has there been a reply. The design # is : 5021543 and I want a watermark on the side with the persons picture that is on the notes side or right side of the card. There is one on the other side and it should be somewhat similar. I am speaking of the stylized W.

Target Market(s)

prospective buyers and sellers, past clients, other Realtors

Industry/Entity Type

Real Estate

Other font styles liked:
• Tragen

Requirements
Must have
• Beside the agents name their designation must be either beside or under. Can be smaller: Norma Castell, Broker
The brokerage name Fernhollow Realty, must have the word Brokerage beside or under, can be smaller: Fernhollow Realty, Brokerage

```html
<!DOCTYPE html>
<html lang="en">
<head>
<meta charset="utf-8">
<title>Fernhollow Realty – Norma Castell business card</title>
<link rel="stylesheet" href="https://fonts.googleapis.com/css2?family=Arimo:wght@400;700&display=swap">
<style>
  :root {
    --navy-deep: #0f2440;
    --navy: #1b3a5e;
    --navy-mid: #2a5078;
    --brand-blue: #4a7fb5;
    --band-blue: #1e4f86;
    --line-blue: #2c4f86;
    --skyline: #4d6f95;
    --paper: #ffffff;
    --photo-dark: #15171c;
    --photo-mid: #3a3d44;
    --bg: #e9ecef;
    --white: #ffffff;
  }
  * { margin: 0; padding: 0; box-sizing: border-box; }
  html, body { width: 1200px; height: 960px; overflow: hidden; }
  body {
    background: var(--bg);
    font-family: "Arimo", Arial, sans-serif;
    position: relative;
  }
  .card {
    position: absolute;
    left: 215px;
    width: 770px;
    height: 440px;
    overflow: hidden;
    box-shadow: 0 6px 18px rgba(0,0,0,.18);
  }
  .card--back { top: 30px; background: var(--paper); }
  .card--front {
    top: 490px;
    background: linear-gradient(135deg, var(--navy-deep) 0%, var(--navy) 60%, var(--navy-mid) 100%);
    color: var(--white);
  }

  /* Back side */
  .back-art { position: absolute; inset: 0; }
  .brand {
    position: absolute;
    display: flex;
    align-items: center;
    gap: 10px;
    font-weight: 700;
    white-space: nowrap;
  }
  .brand__square { background: var(--brand-blue); flex: none; }
  .card--back .brand { left: 440px; top: 44px; color: var(--band-blue); font-size: 24px; }
  .card--back .brand__square { width: 26px; height: 26px; }
  .notes {
    position: absolute;
    left: 440px; top: 102px;
    font-size: 22px; font-weight: 700;
    color: var(--line-blue);
    letter-spacing: .5px;
  }
  .notes-lines {
    position: absolute;
    left: 440px; top: 160px;
    width: 290px;
    list-style: none;
  }
  .notes-lines li {
    height: 38px;
    border-bottom: 1.5px solid var(--line-blue);
  }

  /* Front side */
  .skyline { position: absolute; left: 0; bottom: 0; width: 100%; height: 200px; }
  .card--front .brand { right: 40px; top: 40px; font-size: 26px; color: var(--white); }
  .card--front .brand__square { width: 30px; height: 30px; }
  .agent { position: absolute; left: 56px; top: 118px; }
  .agent__name { font-size: 46px; font-weight: 700; line-height: 1.05; }
  .agent__title { font-size: 28px; margin-top: 2px; }
  .contact { position: absolute; left: 56px; top: 222px; font-size: 22px; }
  .contact__phone { margin-bottom: 22px; }
  .contact__row { display: flex; align-items: center; gap: 12px; margin-bottom: 8px; font-size: 20px; }
  .contact__row svg { width: 18px; height: 18px; flex: none; }
  .office {
    position: absolute;
    left: 56px; bottom: 24px;
    font-size: 19px;
    color: var(--white);
  }
</style>
</head>
<body>

<section class="card card--back" aria-label="Card back with notes">
  <svg class="back-art" viewBox="0 0 770 440" aria-hidden="false">
    <defs>
      <radialGradient id="photoTone" cx="40%" cy="45%" r="65%">
        <stop offset="0" stop-color="var(--photo-mid)"/>
        <stop offset="1" stop-color="var(--photo-dark)"/>
      </radialGradient>
    </defs>
    <g role="img" aria-label="Portrait photograph of Norma Castell">
      <rect width="770" height="440" fill="url(#photoTone)"/>
    </g>
    <path d="M300 0 C 380 120, 400 300, 380 440 L 770 440 L 770 0 Z" fill="var(--paper)"/>
    <path d="M300 0 C 380 120, 400 300, 380 440" fill="none" stroke="var(--band-blue)" stroke-width="10"/>
  </svg>
  <div class="brand"><span class="brand__square"></span>Fernhollow Realty</div>
  <div class="notes">NOTES</div>
  <ul class="notes-lines">
    <li></li><li></li><li></li><li></li><li></li><li></li>
  </ul>
</section>

<section class="card card--front" aria-label="Card front">
  <svg class="skyline" viewBox="0 0 770 200" preserveAspectRatio="none" role="img" aria-label="Ottawa city skyline illustration">
    <defs>
      <linearGradient id="skyTone" x1="0" y1="0" x2="0" y2="1">
        <stop offset="0" stop-color="var(--skyline)" stop-opacity="0"/>
        <stop offset=".45" stop-color="var(--skyline)" stop-opacity=".55"/>
        <stop offset="1" stop-color="var(--skyline)" stop-opacity=".85"/>
      </linearGradient>
    </defs>
    <rect width="770" height="200" fill="url(#skyTone)"/>
  </svg>

  <div class="brand"><span class="brand__square"></span>Fernhollow Realty</div>

  <div class="agent">
    <div class="agent__name">Norma Castell</div>
    <div class="agent__title">Broker</div>
  </div>

  <div class="contact">
    <div class="contact__phone">(613) 555-0192 EXT 3</div>
    <div class="contact__row">
      <svg viewBox="0 0 20 20" aria-hidden="true"><circle cx="10" cy="10" r="8.5" fill="none" stroke="#fff" stroke-width="1.6"/><path d="M1.5 10h17M10 1.5c-4 4.5-4 12.5 0 17M10 1.5c4 4.5 4 12.5 0 17" fill="none" stroke="#fff" stroke-width="1.4"/></svg>
      <span>www.normacastell.ca</span>
    </div>
    <div class="contact__row">
      <svg viewBox="0 0 20 20" aria-hidden="true"><rect x="1.5" y="4" width="17" height="12" fill="none" stroke="#fff" stroke-width="1.6"/><path d="M1.5 4l8.5 7 8.5-7" fill="none" stroke="#fff" stroke-width="1.6"/></svg>
      <span>ncastell@fernhollow.ca</span>
    </div>
  </div>

  <div class="office">Fernhollow Realty, Brokerage, 48 Larkspur Crescent, Ottawa, ON, K2J 0A0</div>
</section>

</body>
</html>
```